Bref créative
Corvel Byte - PC Service Company
Business Card, Stationery, Envelope
Professional
Wade Harlock, MCP
4710 Pelham Ferry Rd.
Gainesville, GA 30548
wtharlock@corvelbyte.example
www.corvelbyte.example
Stationery:
Stationery should be letter size (8.5W x 11H). I think the header should be logo + graphics only and all other info should be in the footer but I am flexable. The design should include:
- My address
- My phone number
- My URL
Use either logo, use only the colors found in the logo. The font should be Century Gothic or similar.
Envelope:
The envelope should be #10 size (4 1/8H x 9 1/2W). The envelope should use the logo with the transparent background and should include our address as the return address in the upper left corner. The envelope design should be very simple and should match the stationery. The font used should be Century Gothic or similar.
Business Card:
The front of the card should have a white background and should contain all of the following:
- My name and title
- My cell number
- My email address
Optional info for the front of the card if you can display it in an attractive way without making the card appear too cluttered:
- My Address
Please note my URL must be on one side of the card, it can be the front or the back.
The font used in our logo is Century Gothic. I can provide our logo in additional formats if needed, just leave a request for the format you need.
Use only the colors found in the logo plus white and black. I want the card to look professional, clean and high-tech.
Please be sure to read my comments as the contest progresses as I may have additional requests once I start seeing some designs.
The back of the card should be in one of the following formats:
1. Only our URL: www.corvelbyte.example
2. Our URL and our Logo
3. Only our logo
Please choose the option you feel is most attractive. If you do not use the URL on the back of the card you must use it on the front.
The back of the card should be white, blue or the same grey seen in CorvelFinalDark.png and may include some minimal graphics in addition to the logo (if used).

```html
<!DOCTYPE html>
<html lang="en">
<head>
<meta charset="utf-8">
<title>Corvel Byte – Stationery Set</title>
<link href="https://fonts.googleapis.com/css2?family=Questrial&display=swap" rel="stylesheet">
<style>
  :root {
    --stage-dark: #1e1e20;
    --stage-light: #4a4a4d;
    --paper: #ffffff;
    --brand-green: #8cc63f;
    --brand-green-dark: #5fa32e;
    --brand-blue: #1b8fc9;
    --brand-blue-dark: #0f6fa6;
    --ink: #3c3c3c;
    --ink-soft: #7a7a7a;
    --faint: #ececec;
  }
  * { margin: 0; padding: 0; box-sizing: border-box; }
  html, body { width: 1200px; height: 871px; overflow: hidden; }
  body {
    position: relative;
    font-family: "Questrial", "Century Gothic", sans-serif;
    color: var(--ink);
    background: radial-gradient(ellipse at 50% 45%, var(--stage-light) 0%, var(--stage-dark) 75%);
  }
  .sheet {
    position: absolute;
    background: var(--paper);
    box-shadow: 0 4px 14px rgba(0,0,0,.45);
    overflow: hidden;
  }
  .wordmark {
    display: flex; align-items: center; gap: 8px;
    color: var(--ink); font-size: 22px; letter-spacing: .5px;
  }
  .wordmark .dot {
    width: 26px; height: 26px; border-radius: 50%;
    background: var(--brand-green);
  }
  .wordmark .name { line-height: 1; }
  .contact-line { font-size: 6px; color: var(--ink-soft); line-height: 1.4; }

  /* Envelope front */
  .envelope-front { left: 53px; top: 84px; width: 552px; height: 228px; }
  .envelope-front .wordmark { position: absolute; left: 20px; top: 18px; }
  .envelope-front .return-address { position: absolute; left: 20px; top: 52px; }
  .envelope-front .band { position: absolute; left: 0; bottom: 0; width: 100%; height: 46px; }

  /* Envelope back */
  .envelope-back { left: 53px; top: 336px; width: 552px; height: 221px; }
  .envelope-back svg { position: absolute; inset: 0; }

  /* Business cards */
  .card-back { left: 53px; top: 619px; width: 259px; height: 156px; background: var(--brand-green); }
  .card-back .mark {
    position: absolute; left: 92px; top: 40px; width: 76px; height: 76px;
    border-radius: 50%; border: 10px solid var(--paper);
  }
  .card-back .url {
    position: absolute; right: 8px; top: 0; height: 156px;
    display: flex; align-items: center;
    writing-mode: vertical-rl; transform: rotate(180deg);
    font-size: 6px; color: var(--paper); letter-spacing: .3px;
  }
  .card-front { left: 331px; top: 619px; width: 264px; height: 156px; }
  .card-front .wordmark { position: absolute; left: 12px; top: 12px; font-size: 17px; }
  .card-front .wordmark .dot { width: 20px; height: 20px; }
  .card-front .ghost {
    position: absolute; left: 60px; top: 38px; width: 92px; height: 92px;
    border-radius: 50%; border: 14px solid var(--faint);
  }
  .card-front .person {
    position: absolute; left: 70px; top: 70px;
    font-size: 11px; color: var(--brand-green-dark);
  }
  .card-front .card-contact {
    position: absolute; left: 70px; top: 86px;
    font-size: 6.4px; line-height: 1.5; color: var(--ink);
  }
  .card-front .band { position: absolute; left: 0; bottom: 0; width: 100%; height: 30px; }

  /* Letterhead */
  .letterhead { left: 643px; top: 84px; width: 504px; height: 720px; }
  .letterhead .wordmark { position: absolute; left: 22px; top: 22px; }
  .letterhead .header-art { position: absolute; left: 0; top: 54px; width: 100%; height: 40px; }
  .letterhead .header-contact { position: absolute; left: 22px; top: 62px; font-size: 5.6px; color: var(--ink-soft); }
  .letterhead .body-copy { position: absolute; left: 22px; top: 104px; width: 460px; }
  .letterhead .body-copy p { font-size: 8.6px; line-height: 1.6; margin-bottom: 12px; color: var(--ink); text-align: justify; }
  .letterhead .sign-role { position: absolute; left: 22px; top: 578px; font-size: 7px; }
  .letterhead .signature { position: absolute; left: 22px; top: 590px; width: 80px; height: 34px; }
  .letterhead .footer-art { position: absolute; left: 0; bottom: 0; width: 100%; height: 80px; }
</style>
</head>
<body>

  <section class="sheet envelope-front" aria-label="Envelope front">
    <div class="wordmark"><span class="dot"></span><span class="name">corvelbyte</span></div>
    <div class="return-address contact-line">
      4710 Pelham Ferry Rd.<br>Gainesville, GA 30548
    </div>
    <svg class="band" viewBox="0 0 552 46" preserveAspectRatio="none">
      <defs>
        <linearGradient id="envBlue" x1="0" x2="1">
          <stop offset="0" stop-color="#0f6fa6"/><stop offset="1" stop-color="#1b8fc9"/>
        </linearGradient>
      </defs>
      <path d="M0 20 C150 4 300 30 552 8 L552 46 L0 46 Z" fill="url(#envBlue)"/>
      <path d="M0 14 C150 0 300 26 552 4 L552 10 C300 32 150 8 0 22 Z" fill="#8cc63f"/>
    </svg>
  </section>

  <section class="sheet envelope-back" aria-label="Envelope back">
    <svg viewBox="0 0 552 221" preserveAspectRatio="none">
      <rect x="0" y="0" width="552" height="36" fill="#1b8fc9"/>
      <path d="M0 36 C180 26 360 44 552 30 L552 38 C360 50 180 32 0 42 Z" fill="#8cc63f"/>
      <path d="M0 42 L276 140 L552 38" fill="none" stroke="#dcdcdc" stroke-width="1.5"/>
      <circle cx="276" cy="140" r="30" fill="none" stroke="#eeeeee" stroke-width="9"/>
    </svg>
  </section>

  <section class="sheet card-back" aria-label="Business card back">
    <div class="mark"></div>
    <div class="url">www.corvelbyte.example</div>
  </section>

  <section class="sheet card-front" aria-label="Business card front">
    <div class="ghost"></div>
    <div class="wordmark"><span class="dot"></span><span class="name">corvelbyte</span></div>
    <div class="person">Wade Harlock, MCP</div>
    <div class="card-contact">
      Cell (770) 555-0193<br>
      wtharlock@corvelbyte.example<br>
      www.corvelbyte.example
    </div>
    <svg class="band" viewBox="0 0 264 30" preserveAspectRatio="none">
      <path d="M0 30 C90 24 170 4 264 0 L264 30 Z" fill="#8cc63f"/>
      <path d="M120 30 C170 22 220 12 264 10 L264 30 Z" fill="#5fa32e"/>
    </svg>
  </section>

  <section class="sheet letterhead" aria-label="Letterhead">
    <div class="wordmark"><span class="dot"></span><span class="name">corvelbyte</span></div>
    <svg class="header-art" viewBox="0 0 504 40" preserveAspectRatio="none">
      <line x1="22" y1="4" x2="300" y2="4" stroke="#1b8fc9" stroke-width="1"/>
      <path d="M300 4 C380 4 430 -2 504 0 L504 8 C430 6 380 12 300 6 Z" fill="#1b8fc9"/>
      <path d="M300 6 C380 12 440 14 504 8 L504 14 C430 18 370 16 300 6 Z" fill="#8cc63f"/>
    </svg>
    <div class="header-contact">4710 Pelham Ferry Rd. Gainesville, GA 30548 &nbsp; Phone (770) 555-0148 &nbsp; wtharlock@corvelbyte.example &nbsp; www.corvelbyte.example</div>

    <div class="body-copy">
      <p>Thank you for choosing our team for your recent repair and upgrade. We know that a working computer matters to your day, so we aim to keep every visit quick, clear and fairly priced for you.</p>
      <p>Our technicians handle desktops, laptops, small office networks and printers, and each job begins with a full check of the system so nothing is missed. We clean out dust, test memory and drives, remove unwanted software and confirm that backups are running as they should. When parts are needed we explain the options, the cost and the time involved before any work starts. Most repairs are finished within two working days, and we call you as soon as the machine is ready to collect. For larger offices we also offer planned visits each month to keep every workstation current and secure.</p>
      <p>If you notice slow start times, strange pop-up windows or noises from the fan, please contact us early. Small problems are simpler to fix before they grow, and a short remote session can often solve them the same day. We keep notes on each machine we service, so returning customers never have to repeat the history of a device. Our prices are listed in writing, and there are no hidden fees for diagnosis when you choose to go ahead with the repair. We value your trust and work hard to earn it on every visit.</p>
      <p>We also help with new equipment. If you are planning to replace older machines, we can suggest models that suit your budget and the way you work, move your files and settings across, and set up printers, email and shared folders so your staff can carry on without delay. Old drives are wiped safely before disposal, and we keep you informed at each step.</p>
      <p>Please keep this letter with your service records. Should any question come up about the work we carried out, simply reply by email or phone and we will be glad to help.</p>
    </div>

    <div class="sign-role">Project Manager</div>
    <svg class="signature" viewBox="0 0 80 34">
      <path d="M4 26 C14 6 22 30 30 18 S44 10 52 22 S66 24 76 14" fill="none" stroke="#3c3c3c" stroke-width="1.2"/>
    </svg>

    <svg class="footer-art" viewBox="0 0 504 80" preserveAspectRatio="none">
      <path d="M0 80 L0 60 C120 70 220 10 504 20 L504 80 Z" fill="#8cc63f"/>
      <path d="M0 80 L0 72 C150 78 300 30 504 40 L504 80 Z" fill="#5fa32e"/>
      <rect x="0" y="74" width="504" height="6" fill="#1b8fc9"/>
    </svg>
  </section>

</body>
</html>
```